KLVN- company with a mission

KLVN LLC stands for keeping lanterns vividly nigh (non profit arm is called lantern kept foundation)—our business is based out of New York City and has a non-profit arm where for every bar you purchase, we donate a bar (don’t want any designs that limits us to only soap). Currently working with South Africa. We want the focus to be organic/natural soap with a mission.
What our website needs to…achieve:
Purpose = branding, building up interesting leaving up to launch date, then a full functional site for selling soap (for now) with a mission. With that said, there will need to be a page designed for “COMING SOON” – with a place to post our teaser 30 second video (kind of like a commercial/movie trailer) – until everything else is done.
We are the first in the industry to do one for one (or …50/50). Most companies that do charity work are mostly for every $$$ we donate $0.10, or 1% of XXX. We are starting out to run the non-profit arm as well not just after we reach certain milestones. In addition, we will be transparent for the non-profit side whereas most of the time when you donate, you have no idea where the money ends up going.
IN ADDITION: we still need to be clean/elegant – and selling our soap; so website will need to 1. Showcase our products, 2. Be very clear that we have a mission (not sure if there is a way to show case both our soap AND our mission)
Some sites we like:
Pelarin.com—like them in terms of business model—in terms of their website: like how their site is clean and friendly, but it seems too cluttered
www.quendaltrove.com -- similar business model, www.fevriskel.com, brimavault.com, marshlintsoap.com
Tivel.com: like this a lot better than gavroue.com, however, major dislike of the typeface. Okay about the neutral colors…although feel like we need something a bit more cheerful here and there for our mission
Zkindle.net, brimavault.com, fennawick.com: like how they are clean and showcase well
**** However, our site also needs to convey messages like: www.wellspringpledge.org, www.rinsewidely.org
Looking for a clean, simple design. Modern, clutter-free, and inviting. Definitely do not want an arts and crafty/flowery feel. We do need something…cheerful for our nonprofit purposes.
Examples of sites we don’t like: quillmarbet.com, corvelpatchsoap.com
7 pages/ tabs maybe? (About us…video page (to show case what we are doing –currently my partner is in South Africa filming what our mission will be able to do – give children and those in need soap), FAQs, soap products, terms & conditions, contact us page, blog page……nothing too crazy).
For now, for designing purposes, please use any example texts whether it’s the about us page, mission page..policies.. and for the soap/products pages—please use example you can find online – it is fine, we just need the design done for now.
I have also attached our logo file. Please let me know if you have any questions! Thanks!
Something to consider....
pelarin.com and quendaltrove.com are probably our largest competitor out of all the websites I mentioned as they have a very similar business model where it is is a company with a mission. Homepage makes that clear that for every pair of shoes/ glasses you purchase, they give a pair. Another thing to note...is that they have been in business for a few years so their website probably have changed to more commercial than focusing/marketing on the mission of doing good. While we don't want that to be the total focus, we do need it to be present on the homepage/front page.

```html
<!DOCTYPE html>
<html lang="en">
<head>
<meta charset="utf-8">
<title>KLVN LLC — Home</title>
<link rel="stylesheet" href="https://fonts.googleapis.com/css2?family=Roboto+Condensed:wght@400;700&family=Arimo:wght@400;700&family=Open+Sans:wght@300;400&family=Questrial&display=swap">
<style>
  :root {
    --orange: #e8812b;
    --orange-soft: #f0a25e;
    --footer-orange: #ee8a36;
    --ink: #333333;
    --text: #666666;
    --muted: #999999;
    --dark: #3b3b3b;
    --bottom-bar: #3d3d3d;
    --panel: #ececec;
    --line: #e2e2e2;
    --white: #ffffff;
  }
  * { box-sizing: border-box; margin: 0; padding: 0; }
  html, body { width: 1200px; height: 2609px; overflow: hidden; background: var(--white); }
  body { position: relative; font-family: "Arimo", Arial, sans-serif; color: var(--text); }
  .abs { position: absolute; }

  /* header */
  .top-rule { left: 0; top: 0; width: 1200px; height: 5px; background: var(--orange-soft); }
  .brand { left: 128px; top: 22px; display: flex; align-items: center; gap: 14px; }
  .brand-dot { width: 104px; height: 104px; border-radius: 50%; background: var(--orange-soft); }
  .brand-name { font-family: "Roboto Condensed", sans-serif; font-weight: 700; font-size: 40px; color: var(--orange); letter-spacing: 2px; }
  .main-nav { left: 466px; top: 58px; display: flex; gap: 27px; font-family: "Roboto Condensed", sans-serif; font-size: 12.5px; color: var(--ink); text-transform: uppercase; }
  .main-nav .current { color: var(--orange); }
  .search { left: 791px; top: 12px; width: 157px; height: 27px; border: 1px solid #d6d6d6; font-size: 11px; color: var(--muted); padding: 7px 10px; }
  .search svg { position: absolute; right: 7px; top: 5px; }
  .search-split { position: absolute; right: 30px; top: 0; width: 1px; height: 25px; background: #d6d6d6; }
  .cart { left: 960px; top: 12px; width: 32px; height: 27px; background: var(--orange-soft); border-radius: 3px; }
  .cart-count { left: 1000px; top: 17px; font-size: 13px; color: var(--ink); font-family: "Open Sans", sans-serif; }

  /* hero */
  .hero { left: 0; top: 99px; width: 1200px; height: 445px; background: linear-gradient(100deg, #5b5b5b 0%, #8a8a8a 30%, #4d4d4d 55%, #9a9a9a 80%, #6e6e6e 100%); }
  .hero-arrow { top: 298px; }
  .hero-caption { left: 638px; top: 313px; width: 411px; height: 200px; background: rgba(40,40,40,0.72); padding: 18px 20px; }
  .hero-title { font-family: "Open Sans", sans-serif; font-weight: 300; font-size: 38px; color: var(--orange-soft); letter-spacing: 2px; }
  .hero-text { margin-top: 14px; font-family: "Open Sans", sans-serif; font-size: 16px; line-height: 26px; color: #e8e8e8; }
  .hero-more { margin-top: 16px; font-family: "Open Sans", sans-serif; font-size: 15px; color: #dddddd; }

  /* headings */
  .section-title { font-family: "Roboto Condensed", sans-serif; font-weight: 700; font-size: 27px; color: var(--orange); }

  /* welcome */
  .welcome-text { left: 130px; top: 655px; width: 910px; font-size: 12.5px; line-height: 33.5px; color: var(--text); }

  /* mission */
  .mission-item { width: 260px; text-align: center; }
  .mission-icon { width: 104px; height: 104px; border-radius: 50%; background: var(--orange-soft); margin: 0 auto; display: flex; align-items: center; justify-content: center; }
  .mission-name { margin-top: 23px; font-family: "Roboto Condensed", sans-serif; font-weight: 700; font-size: 16px; color: var(--orange); }
  .mission-desc { margin: 24px auto 0; width: 245px; font-size: 12.5px; line-height: 22px; color: var(--text); }

  /* banner */
  .banner { left: 0; top: 1198px; width: 1200px; height: 181px; background: linear-gradient(90deg, #e9a46a 0%, #f3c49b 35%, #f6d3b2 60%, #e9b88a 100%); }
  .banner-title { left: 153px; top: 1236px; font-family: "Questrial", sans-serif; font-size: 34px; color: var(--white); }
  .banner-sub { left: 300px; top: 1295px; width: 448px; text-align: right; font-family: "Questrial", sans-serif; font-size: 13px; line-height: 23px; color: var(--white); }
  .banner-rule { left: 762px; top: 1214px; width: 2px; height: 148px; background: rgba(80,60,40,0.55); }
  .btn { display: flex; align-items: center; justify-content: center; background: var(--dark); color: var(--white); border-radius: 3px; font-family: "Roboto Condensed", sans-serif; font-weight: 700; }
  .donate-now { left: 863px; top: 1266px; width: 153px; height: 38px; font-size: 17px; }

  /* products & blog */
  .product-photo { width: 198px; height: 180px; border: 1px solid var(--line); }
  .blog-date { font-family: "Roboto Condensed", sans-serif; font-weight: 700; font-size: 17px; color: var(--ink); }
  .blog-title { font-family: "Roboto Condensed", sans-serif; font-size: 16px; color: var(--ink); }
  .blog-text { width: 190px; font-size: 12.5px; line-height: 26px; color: var(--text); text-align: justify; }
  .blog-photo { width: 235px; height: 167px; }

  /* progress */
  .progress-panel { left: 130px; top: 2012px; width: 333px; height: 261px; background: var(--panel); }
  .progress-text { left: 140px; top: 2036px; width: 313px; text-align: center; font-family: "Open Sans", sans-serif; font-size: 15px; line-height: 28px; color: #444444; z-index: 2; }
  .progress-figure { left: 172px; top: 2124px; font-family: "Questrial", sans-serif; font-size: 46px; color: #444444; }
  .progress-figure small { font-size: 28px; }
  .progress-donate { left: 167px; top: 2205px; width: 110px; height: 38px; font-size: 15px; font-family: "Open Sans", sans-serif; font-weight: 400; }
  .children-figure { left: 305px; top: 2106px; width: 150px; height: 164px; background: var(--orange-soft); border-radius: 36px 36px 4px 4px; z-index: 1; }

  /* faq */
  .faq-panel { left: 480px; top: 2014px; width: 310px; height: 259px; border: 1px solid var(--line); }
  .faq-q { width: 280px; font-size: 12px; line-height: 28px; color: var(--ink); }
  .faq-chevron { left: 755px; }
  .view-all { left: 560px; top: 2219px; width: 148px; height: 35px; font-size: 15px; }

  /* newsletter */
  .news-text { left: 814px; top: 2014px; width: 240px; font-size: 12.5px; line-height: 23px; color: var(--ink); }
  .news-field { left: 814px; width: 235px; height: 44px; border: 1.5px solid var(--orange-soft); font-family: "Roboto Condensed", sans-serif; font-size: 12px; color: var(--muted); padding: 14px 12px; }
  .news-field svg { position: absolute; right: 12px; top: 13px; }
  .subscribe { left: 943px; top: 2238px; width: 107px; height: 37px; font-size: 16px; border-radius: 5px; }

  /* footer */
  .site-footer { left: 0; top: 2342px; width: 1200px; height: 206px; background: var(--footer-orange); }
  .footer-col { top: 2364px; color: var(--white); }
  .footer-col h3 { font-family: "Roboto Condensed", sans-serif; font-weight: 700; font-size: 17px; margin-bottom: 12px; }
  .footer-col li { list-style: none; font-size: 12.5px; line-height: 28px; display: flex; align-items: center; gap: 8px; }
  .bottom-bar { left: 0; top: 2548px; width: 1200px; height: 61px; background: var(--bottom-bar); }
  .copyright { left: 137px; top: 2570px; font-size: 12.5px; color: var(--white); }
  .social { top: 2570px; width: 16px; height: 16px; border-radius: 50%; background: var(--white); }
</style>
</head>
<body>

<header>
  <div class="abs top-rule"></div>
  <div class="abs brand"><span class="brand-dot"></span><span class="brand-name">KLVN</span></div>
  <nav class="abs main-nav">
    <span class="current">About Us</span><span>Our Mission</span><span>FAQ</span><span>Soap Products</span><span>Terms &amp; Conditions</span><span>Contact Us</span><span>Blog</span>
  </nav>
  <div class="abs search">Search
    <span class="search-split"></span>
    <svg width="16" height="16" viewBox="0 0 16 16"><circle cx="6.5" cy="6.5" r="4.5" fill="none" stroke="#777" stroke-width="2"/><line x1="10" y1="10" x2="14" y2="14" stroke="#777" stroke-width="2"/></svg>
  </div>
  <div class="abs cart">
    <svg width="32" height="27" viewBox="0 0 32 27"><path d="M8 9h16l-2 9H10z" fill="#fff"/><rect x="11" y="6" width="10" height="3" fill="#fff"/></svg>
  </div>
  <div class="abs cart-count">0 items</div>
</header>

<section>
  <div class="abs hero" role="img" aria-label="Black and white photograph of smiling children"></div>
  <svg class="abs hero-arrow" style="left:66px" width="16" height="24" viewBox="0 0 16 24"><path d="M13 2 3 12l10 10" fill="none" stroke="#fff" stroke-width="3"/></svg>
  <svg class="abs hero-arrow" style="left:1110px" width="16" height="24" viewBox="0 0 16 24"><path d="M3 2l10 10L3 22" fill="none" stroke="#fff" stroke-width="3"/></svg>
  <div class="abs hero-caption">
    <div class="hero-title">SOAP SAVES LIVES</div>
    <p class="hero-text">There are many variations of passages of Lorem Ipsum available.</p>
    <div class="hero-more">more &gt;&gt;</div>
  </div>
</section>

<section>
  <h2 class="abs section-title" style="left:130px;top:608px">Welcome to KLVN LLC</h2>
  <p class="abs welcome-text">There are many variations of passages of Lorem Ipsum available, but the majority have suffered alteration in some form, by injected humour, or randomised words which don't look even slightly believable. If you are going to use a passage of Lorem Ipsum, you need to be sure there isn't anything embarrassing.If you are going to use a passage of Lorem Ipsum, you need to be sure there isn't anything embarrassing hidden in the middle of text.It is a long established fact that a reader will be distracted by the readable content of a page when looking at its layout.</p>
</section>

<section>
  <h2 class="abs section-title" style="left:132px;top:832px">Our Mission</h2>
  <div class="abs mission-item" style="left:107px;top:896px">
    <div class="mission-icon">
      <svg width="56" height="56" viewBox="0 0 56 56" fill="#fff"><circle cx="28" cy="14" r="7"/><path d="M6 18c4 0 6 4 7 10l3 10h24l3-10c1-6 3-10 7-10v14c0 8-6 16-14 18H20C12 48 6 40 6 32z"/></svg>
    </div>
    <div class="mission-name">Loreum ipsum</div>
    <p class="mission-desc">All the Lorem Ipsum generators on the Internet tend to repeat predefined chunks as necessary,.</p>
  </div>
  <div class="abs mission-item" style="left:458px;top:896px">
    <div class="mission-icon">
      <svg width="56" height="56" viewBox="0 0 56 56" fill="#fff"><circle cx="24" cy="10" r="6"/><path d="M18 18h12l8 14h10v6H34l-6-10-4 10h8v14h-6V44H14l8-18z"/></svg>
    </div>
    <div class="mission-name">Loreum ipsum</div>
    <p class="mission-desc">All the Lorem Ipsum generators on the Internet tend to repeat predefined chunks as necessary,.</p>
  </div>
  <div class="abs mission-item" style="left:809px;top:896px">
    <div class="mission-icon">
      <svg width="52" height="52" viewBox="0 0 52 52" fill="#fff"><rect x="4" y="8" width="44" height="40" rx="4"/><rect x="12" y="3" width="4" height="10" rx="2"/><rect x="36" y="3" width="4" height="10" rx="2"/><g fill="#f0a25e"><rect x="10" y="20" width="7" height="6"/><rect x="22" y="20" width="7" height="6"/><rect x="34" y="20" width="7" height="6"/><rect x="10" y="30" width="7" height="6"/><rect x="22" y="30" width="7" height="6"/><rect x="34" y="30" width="7" height="6"/><rect x="10" y="40" width="7" height="4"/><rect x="22" y="40" width="7" height="4"/></g></svg>
    </div>
    <div class="mission-name">Loreum ipsum</div>
    <p class="mission-desc">All the Lorem Ipsum generators on the Internet tend to repeat predefined chunks as necessary,.</p>
  </div>
</section>

<section>
  <div class="abs banner" role="img" aria-label="Warm orange-toned photograph of children and soap-making workshop"></div>
  <div class="abs banner-title">Proin gravida nibh vel velit auctor</div>
  <p class="abs banner-sub">Aenean sollicitudin, lorem quis bibendum auctor elit consequat ipsum, nec sagittis sem nibh id elit</p>
  <div class="abs banner-rule"></div>
  <div class="abs btn donate-now">Donate Now</div>
</section>

<section>
  <h2 class="abs section-title" style="left:130px;top:1444px">Products</h2>
  <div class="abs product-photo" style="left:132px;top:1511px;background:linear-gradient(135deg,#e8e2d6,#b9c79a)" role="img" aria-label="Wrapped natural soap bars tied with twine"></div>
  <div class="abs product-photo" style="left:348px;top:1511px;background:linear-gradient(135deg,#5d9a3c,#e59a4a 50%,#c05a7a)" role="img" aria-label="Stack of colourful soap bars"></div>
  <div class="abs product-photo" style="left:132px;top:1711px;background:linear-gradient(135deg,#a8c24a,#7e9a36)" role="img" aria-label="Green herbal soap bars with lavender"></div>
  <div class="abs product-photo" style="left:348px;top:1711px;background:linear-gradient(135deg,#d9dbe6,#e7d6ae 60%,#8aa43a)" role="img" aria-label="Cream soap bar with olive and lavender sprig"></div>

  <h2 class="abs section-title" style="left:602px;top:1444px">Blog</h2>
  <div class="abs" style="left:602px;top:1499px">
    <div class="blog-date">Jan 16, 2014</div>
    <div class="blog-title" style="margin-top:14px">Loreum Ipsum</div>
    <p class="blog-text" style="margin-top:12px">It is a long established fact that a reader will be distracted by the readable content of a page when looking at its layout.</p>
  </div>
  <div class="abs blog-photo" style="left:828px;top:1499px;background:linear-gradient(135deg,#c48a5a,#7a4a2c)" role="img" aria-label="Open hands reaching forward"></div>
  <div class="abs" style="left:602px;top:1706px">
    <div class="blog-date">Mar 30, 2014</div>
    <div class="blog-title" style="margin-top:14px">Loreum Ipsum</div>
    <p class="blog-text" style="margin-top:12px">It is a long established fact that a reader will be distracted by the readable content of a page when looking at its layout.</p>
  </div>
  <div class="abs blog-photo" style="left:828px;top:1706px;background:linear-gradient(135deg,#9a9a9a,#444444)" role="img" aria-label="Black and white photograph of a child holding a baby"></div>
</section>

<section>
  <h2 class="abs section-title" style="left:130px;top:1959px">Global Progress</h2>
  <div class="abs progress-panel"></div>
  <p class="abs progress-text">Lorem ipsum dolor sit amet, consectetur adipisicing elit, sed do eiusmod tempor</p>
  <div class="abs progress-figure">5.4<small>M</small></div>
  <div class="abs btn progress-donate">DONATE</div>
  <div class="abs children-figure" role="img" aria-label="Silhouette of a group of children cheering"></div>

  <h2 class="abs section-title" style="left:485px;top:1959px">FAQ</h2>
  <div class="abs faq-panel"></div>
  <p class="abs faq-q" style="left:491px;top:2029px">Lorem Ipsum is simply dummy text of the printing and typesetting industry. Lorem Ipsum has been the industry's standard dummy text?</p>
  <p class="abs faq-q" style="left:491px;top:2123px">Lorem Ipsum is simply dummy text of the printing and typesetting industry. Lorem Ipsum has been the industry's standard dummy text?</p>
  <svg class="abs faq-chevron" style="top:2096px" width="12" height="8" viewBox="0 0 12 8"><path d="M1 1l5 5 5-5" fill="none" stroke="#e8812b" stroke-width="1.5"/></svg>
  <svg class="abs faq-chevron" style="top:2190px" width="12" height="8" viewBox="0 0 12 8"><path d="M1 1l5 5 5-5" fill="none" stroke="#e8812b" stroke-width="1.5"/></svg>
  <div class="abs btn view-all">View All...</div>

  <h2 class="abs section-title" style="left:816px;top:1959px">News Letter</h2>
  <p class="abs news-text">Sign up to our newsletter to receive regular updates from the Global Rinse Project.</p>
  <div class="abs news-field" style="top:2097px">Email address
    <svg width="20" height="16" viewBox="0 0 20 16"><rect x="1" y="2" width="18" height="12" fill="none" stroke="#f0a25e" stroke-width="1.4"/><path d="M1 2l9 7 9-7" fill="none" stroke="#f0a25e" stroke-width="1.4"/></svg>
  </div>
  <div class="abs news-field" style="top:2165px">Name
    <svg width="18" height="18" viewBox="0 0 18 18"><circle cx="9" cy="6" r="4" fill="none" stroke="#f0a25e" stroke-width="1.4"/><path d="M2 17c0-4 3-6 7-6s7 2 7 6z" fill="none" stroke="#f0a25e" stroke-width="1.4"/></svg>
  </div>
  <div class="abs btn subscribe">Subscribe</div>
</section>

<footer>
  <div class="abs site-footer"></div>
  <div class="abs footer-col" style="left:132px">
    <h3>About Us</h3>
    <ul><li>Leadership Team</li><li>Board of Directors</li><li>FAQs</li><li>History</li><li>Contact</li></ul>
  </div>
  <div class="abs footer-col" style="left:409px">
    <h3>Our Mission</h3>
    <ul><li>Donate</li><li>Volunteer</li><li>Host a Party</li></ul>
  </div>
  <div class="abs footer-col" style="left:670px">
    <h3>Quick Links</h3>
    <ul><li>Donate</li><li>Volunteer</li><li>Host a Party</li></ul>
  </div>
  <div class="abs footer-col" style="left:927px">
    <h3>Contact Us</h3>
    <ul>
      <li><svg width="16" height="12" viewBox="0 0 16 12"><rect x="0" y="0" width="16" height="12" fill="#fff"/><path d="M0 0l8 6 8-6" fill="none" stroke="#ee8a36" stroke-width="1.2"/></svg>www.klvnllc.com</li>
      <li><svg width="16" height="16" viewBox="0 0 16 16"><path d="M4 1c1 0 2 3 2 4s-2 1-1 3 2 3 3 3 1-2 2-2 4 1 4 2-2 4-4 4C6 15 1 10 1 5c0-2 2-4 3-4z" fill="#fff"/></svg>044- 555190</li>
    </ul>
  </div>
  <div class="abs bottom-bar"></div>
  <div class="abs copyright">© 2013-2014 KLVN LLC. All rights reserved.</div>
  <span class="abs social" style="left:972px"></span>
  <span class="abs social" style="left:1001px"></span>
  <span class="abs social" style="left:1030px"></span>
</footer>

</body>
</html>
```